Looking for a professional, clean and crisp business card

I am in the underground utilities industry and am just looking for a really impressive business card. I would like our card to be white with our symbol crisp and clear with it protruding. I also have a business partner that will require his name and info on the card once the design is set. I would like to have our website info on the card which is;
http://granitetrenchco.example/

Contact Information for Business Card

Website, contact name, number and email

```html
<!DOCTYPE html>
<html lang="en">
<head>
<meta charset="utf-8">
<title>Granite Trench Co — Business Card</title>
<link rel="stylesheet" href="https://fonts.googleapis.com/css2?family=Roboto:wght@400;500;700&display=swap">
<style>
  :root {
    --backdrop: #e7e3de;
    --card-white: #ffffff;
    --card-black: #1e1e1e;
    --ink: #222222;
    --ink-soft: #555555;
    --brand-blue: #3a5ea8;
    --accent-red: #e3262d;
    --rule: #555555;
    --on-dark: #ffffff;
  }
  * { box-sizing: border-box; margin: 0; padding: 0; }
  html, body {
    width: 1125px; height: 1200px; overflow: hidden;
    background: var(--backdrop);
    font-family: "Roboto", Arial, sans-serif;
  }
  .canvas { position: relative; width: 1125px; height: 1200px; }

  .card {
    position: absolute;
    box-shadow: 0 3px 8px rgba(0,0,0,0.25);
  }
  .card--front {
    left: 176px; top: 106px; width: 825px; height: 470px;
    background: var(--card-white);
  }
  .card--back {
    left: 167px; top: 633px; width: 844px; height: 482px;
    background: var(--card-black);
    display: flex; align-items: center; justify-content: center;
  }

  .wordmark {
    display: flex; align-items: center; gap: 14px;
    font-weight: 500; line-height: 1.1;
  }
  .wordmark__dot { width: 18px; height: 18px; border-radius: 50%; flex: none; }
  .card--front .wordmark {
    position: absolute; left: 118px; top: 190px; width: 220px;
    color: var(--ink); font-size: 30px;
  }
  .card--front .wordmark__dot { background: var(--ink); }
  .card--back .wordmark { color: var(--on-dark); font-size: 44px; }
  .card--back .wordmark__dot { background: var(--on-dark); width: 26px; height: 26px; }

  .divider {
    position: absolute; left: 376px; top: 134px;
    width: 1px; height: 204px; background: var(--rule);
  }

  .contact { position: absolute; left: 418px; top: 128px; }
  .contact__name {
    color: var(--brand-blue); font-weight: 700; font-size: 26px;
    letter-spacing: 0.2px; line-height: 1.1;
  }
  .contact__role { color: var(--accent-red); font-weight: 500; font-size: 18px; margin-top: 4px; }
  .contact__address { color: var(--ink-soft); font-size: 18px; line-height: 23px; margin-top: 18px; }
  .contact__list { list-style: none; margin-top: 16px; }
  .contact__item {
    display: flex; align-items: center; gap: 10px;
    color: var(--ink-soft); font-size: 18px; line-height: 24px;
  }
  .contact__icon { width: 15px; height: 15px; flex: none; fill: var(--brand-blue); }
</style>
</head>
<body>
<main class="canvas">

  <section class="card card--front" aria-label="Business card front">
    <div class="wordmark">
      <span class="wordmark__dot"></span>
      <span class="wordmark__name">Granite Trench Co</span>
    </div>

    <div class="divider"></div>

    <div class="contact">
      <p class="contact__name">DANIEL HARGROVE</p>
      <p class="contact__role">President</p>
      <p class="contact__address">412 Birchwood Court<br>Juneau, Alaska 99801</p>
      <ul class="contact__list">
        <li class="contact__item">
          <svg class="contact__icon" viewBox="0 0 24 24" aria-hidden="true"><path d="M6.6 10.8a15.1 15.1 0 0 0 6.6 6.6l2.2-2.2c.3-.3.7-.4 1-.2 1.1.4 2.3.6 3.6.6.6 0 1 .4 1 1V20c0 .6-.4 1-1 1A17 17 0 0 1 3 4c0-.6.4-1 1-1h3.5c.6 0 1 .4 1 1 0 1.3.2 2.5.6 3.6.1.3 0 .7-.2 1z"/></svg>
          <span>369-555-0142</span>
        </li>
        <li class="contact__item">
          <svg class="contact__icon" viewBox="0 0 24 24" aria-hidden="true"><path d="M2 5h20v2l-10 6L2 7z"/><path d="M2 9l10 6 10-6v10H2z"/></svg>
          <span>info@granitetrenchco.example</span>
        </li>
        <li class="contact__item">
          <svg class="contact__icon" viewBox="0 0 24 24" aria-hidden="true"><circle cx="12" cy="12" r="10"/><path d="M2 12h20M12 2c3 3 3 17 0 20M12 2c-3 3-3 17 0 20" stroke="#fff" stroke-width="1.5" fill="none"/></svg>
          <span>www.granitetrenchco.example</span>
        </li>
      </ul>
    </div>
  </section>

  <section class="card card--back" aria-label="Business card back">
    <div class="wordmark">
      <span class="wordmark__dot"></span>
      <span class="wordmark__name">Granite Trench Co</span>
    </div>
  </section>

</main>
</body>
</html>
```